maple crest homeworks KOVA

Looking for business card design that represents our company. we are maple crest homeworks and we dedicate our skills of home energy efficiency to our customer by providing energy solution to their energy problems.
HVAC
SOLAR
INSULLATION
LIGHTING
DUCT TESTING
KOVA RATING.

```html
<!DOCTYPE html>
<html lang="en">
<head>
<meta charset="UTF-8">
<title>Maple Crest Homeworks – Business Card</title>
<link rel="stylesheet" href="https://fonts.googleapis.com/css2?family=Lato:wght@400;700&display=swap">
<style>
  :root {
    --backdrop: #1e1e20;
    --card: #232324;
    --card-edge: #2c2c2d;
    --ink: #f2f2f2;
    --blue: #29a9e6;
    --green: #8cc63f;
  }
  * { box-sizing: border-box; margin: 0; padding: 0; }
  html, body { width: 1200px; height: 900px; overflow: hidden; }
  body {
    background: var(--backdrop);
    font-family: "Lato", sans-serif;
    color: var(--ink);
    position: relative;
  }
  .card {
    position: absolute;
    left: 230px;
    width: 740px;
    height: 410px;
    background: radial-gradient(ellipse at 60% 40%, var(--card-edge), var(--card) 70%);
    border-radius: 4px;
    box-shadow: 0 8px 24px rgba(0,0,0,.55);
  }
  .card--front { top: 30px; }
  .card--back { top: 465px; }

  .brand-name {
    position: absolute;
    font-weight: 700;
    color: var(--ink);
    text-transform: uppercase;
    line-height: 1.1;
    letter-spacing: 2px;
  }
  .card--front .brand-name {
    left: 0; right: 0; top: 125px;
    text-align: center;
    font-size: 34px;
  }
  .card--back .brand-name {
    left: 60px; top: 150px; width: 300px;
    font-size: 28px;
  }

  .services {
    position: absolute;
    left: 0; right: 0; top: 270px;
    text-align: center;
    font-size: 17px;
    letter-spacing: 1.5px;
    line-height: 1.6;
    text-transform: uppercase;
  }
  .services .sep { color: var(--blue); margin: 0 6px; }

  .divider {
    position: absolute;
    left: 400px; top: 120px;
    width: 2px; height: 180px;
    background: var(--blue);
  }
  .contact {
    position: absolute;
    left: 425px; top: 110px;
  }
  .person-name {
    color: var(--blue);
    font-size: 30px;
    font-weight: 700;
    letter-spacing: 1px;
    text-transform: uppercase;
    line-height: 1;
  }
  .person-role { font-size: 17px; margin-top: 4px; }
  .address { font-size: 17px; line-height: 1.35; margin-top: 16px; }
  .contact-list { list-style: none; margin-top: 8px; font-size: 17px; line-height: 1.45; }
  .contact-list li { display: flex; align-items: center; gap: 8px; }
  .contact-list svg { width: 13px; height: 13px; flex: none; }
  .web-domain { color: var(--green); }
</style>
</head>
<body>
  <section class="card card--front">
    <p class="brand-name">Maple Crest<br>Homeworks</p>
    <p class="services">
      HVAC<span class="sep">-</span>Solar<span class="sep">-</span>Insullation<br>
      Lighting<span class="sep">-</span>Duct Testing<span class="sep">-</span>KOVA Rating.
    </p>
  </section>

  <section class="card card--back">
    <p class="brand-name">Maple Crest<br>Homeworks</p>
    <div class="divider"></div>
    <div class="contact">
      <h1 class="person-name">Daniel Reyes</h1>
      <p class="person-role">Director</p>
      <p class="address">412 Larkfield Avenue<br>#02-07B Harbor City 604218</p>
      <ul class="contact-list">
        <li>
          <svg viewBox="0 0 16 16" aria-hidden="true"><path d="M4 1 L6.5 4.5 L5 6 Q6.5 9.5 10 11 L11.5 9.5 L15 12 L13 15 Q5 14 1 3 Z" fill="var(--blue)"/></svg>
          +330 5184-2093
        </li>
        <li>
          <svg viewBox="0 0 16 16" aria-hidden="true"><rect x="1" y="3" width="14" height="10" fill="none" stroke="var(--blue)" stroke-width="1.6"/><path d="M1 3 L8 9 L15 3" fill="none" stroke="var(--blue)" stroke-width="1.6"/></svg>
          info@maplecresthomeworks.com
        </li>
        <li>
          <svg viewBox="0 0 16 16" aria-hidden="true"><circle cx="8" cy="8" r="6.5" fill="none" stroke="var(--blue)" stroke-width="1.4"/><ellipse cx="8" cy="8" rx="3" ry="6.5" fill="none" stroke="var(--blue)" stroke-width="1.2"/><path d="M1.5 8 H14.5" stroke="var(--blue)" stroke-width="1.2"/></svg>
          <span>www.<span class="web-domain">maplecresthomeworks</span>.com</span>
        </li>
      </ul>
    </div>
  </section>
</body>
</html>
```